TR REFEREE ADVISORY sports

Require a banner for a website titled:

TR REFEREE ADVISORY

A sporting style banner to support referees / umpires

using some of the images listed below.

Require a new logo
I do not have a logo for this as yet.

Need to be able to use it on webpages as well.

Thanks Owen

Target Market(s)

SPORT CLUBS / INDIVIDUAL REFEREES / OFFICIALS

Logo Text

TR REFEREE ADVISORY

Font styles to use
Sans Serif

Colors
3277b5

Requirements
Must have
• TAGLINE - SHAPING YOUR CAREER

```html
<!DOCTYPE html>
<html lang="en">
<head>
<meta charset="utf-8">
<title>TR Referee Advisory – Logo and Web Banner</title>
<link rel="stylesheet" href="https://fonts.googleapis.com/css2?family=Saira:wght@600&family=Roboto:wght@400;700&display=swap">
<style>
  :root {
    --brand-blue: #3277b5;
    --label-grey: #a6a6a6;
    --frame-grey: #6f6f6f;
    --tagline-grey: #7a7a7a;
    --banner-border: #c8c8c8;
    --paper: #ffffff;
    --photo-field: #3c5a3a;
    --photo-tennis: #2e3a55;
  }
  html, body {
    margin: 0;
    padding: 0;
    width: 1200px;
    height: 848px;
    overflow: hidden;
    background: var(--paper);
  }
  .sheet {
    position: relative;
    width: 1200px;
    height: 848px;
  }
  .section-label {
    position: absolute;
    left: 0;
    width: 1200px;
    text-align: center;
    font-family: "Roboto", Arial, sans-serif;
    font-size: 20px;
    color: var(--label-grey);
    letter-spacing: 0.5px;
    margin: 0;
  }
  .section-label--logo { top: 126px; }
  .section-label--banner { top: 351px; }

  .logo {
    position: absolute;
    left: 408px;
    top: 174px;
    display: flex;
    align-items: center;
    gap: 14px;
  }
  .logo__square {
    width: 82px;
    height: 82px;
    box-sizing: border-box;
    border: 4px solid var(--frame-grey);
  }
  .logo__name {
    font-family: "Saira", Arial, sans-serif;
    font-weight: 600;
    font-size: 44px;
    line-height: 46px;
    color: var(--brand-blue);
    margin: 0;
    letter-spacing: 0.5px;
  }

  .web-banner {
    position: absolute;
    left: 42px;
    top: 394px;
    width: 1118px;
    height: 319px;
    box-sizing: border-box;
    border: 1px solid var(--banner-border);
    overflow: hidden;
  }
  .web-banner svg { display: block; }
  .banner-tagline {
    font-family: "Roboto", Arial, sans-serif;
    font-weight: 700;
    font-style: italic;
    font-size: 31px;
    fill: var(--tagline-grey);
    letter-spacing: 1px;
  }
  .banner-name {
    font-family: "Saira", Arial, sans-serif;
    font-weight: 600;
    font-size: 40px;
    fill: var(--brand-blue);
  }
</style>
</head>
<body>
<main class="sheet">
  <p class="section-label section-label--logo">LOGO</p>
  <div class="logo">
    <div class="logo__square"></div>
    <p class="logo__name">TR REFEREE<br>ADVISORY</p>
  </div>

  <p class="section-label section-label--banner">WEB BANNER</p>
  <div class="web-banner">
    <svg width="1116" height="317" viewBox="0 0 1116 317" xmlns="http://www.w3.org/2000/svg">
      <defs>
        <linearGradient id="photo-football" x1="0" y1="0" x2="1" y2="1">
          <stop offset="0" stop-color="#1f2a22"/>
          <stop offset="0.45" stop-color="#4f7d3e"/>
          <stop offset="1" stop-color="#1c2230"/>
        </linearGradient>
        <linearGradient id="photo-tennis" x1="0" y1="0" x2="0" y2="1">
          <stop offset="0" stop-color="#1e2b4a"/>
          <stop offset="1" stop-color="#3f5a86"/>
        </linearGradient>
        <linearGradient id="swoosh-grey" x1="0" y1="0" x2="1" y2="0">
          <stop offset="0" stop-color="#8a8a8a"/>
          <stop offset="0.6" stop-color="#e4e4e4"/>
          <stop offset="1" stop-color="#9a9a9a"/>
        </linearGradient>
        <linearGradient id="swoosh-blue" x1="0" y1="0" x2="1" y2="0">
          <stop offset="0" stop-color="#3277b5"/>
          <stop offset="0.5" stop-color="#6a9fd0"/>
          <stop offset="1" stop-color="#d6e5f3"/>
        </linearGradient>
        <linearGradient id="swoosh-low" x1="0" y1="0" x2="1" y2="0">
          <stop offset="0" stop-color="#8a8a8a"/>
          <stop offset="1" stop-color="#e0e0e0"/>
        </linearGradient>
        <path id="tagline-arc" d="M38,100 C150,60 280,42 440,60"/>
      </defs>

      <rect x="0" y="0" width="1116" height="317" fill="#ffffff"/>
      <rect x="488" y="0" width="416" height="317" fill="url(#photo-football)" role="img" aria-label="Photo of a football umpire in a green shirt beside a player"/>
      <rect x="906" y="0" width="210" height="317" fill="url(#photo-tennis)" role="img" aria-label="Photo of a tennis chair umpire speaking with a player"/>

      <path d="M0,317 L0,250 C200,165 420,140 620,180 C780,215 900,265 1116,282 L1116,317 Z" fill="#ffffff"/>

      <path d="M0,178 C180,120 380,105 520,125 C620,140 680,165 710,182 L700,192 C660,172 600,152 510,140 C370,122 180,140 0,208 Z" fill="url(#swoosh-grey)"/>
      <path d="M0,252 C200,165 420,135 620,170 C760,195 880,240 1116,262 L1116,270 C880,252 760,210 620,182 C420,148 200,180 0,272 Z" fill="url(#swoosh-blue)"/>
      <path d="M702,252 C820,278 960,292 1116,290 L1116,300 C960,302 820,292 702,258 Z" fill="url(#swoosh-low)"/>

      <text class="banner-tagline"><textPath href="#tagline-arc">SHAPING YOUR CAREER</textPath></text>

      <rect x="190" y="204" width="74" height="74" fill="none" stroke="var(--frame-grey)" stroke-width="4"/>
      <text class="banner-name" x="280" y="234">TR REFEREE</text>
      <text class="banner-name" x="280" y="276">ADVISORY</text>
    </svg>
  </div>
</main>
</body>
</html>
```